Legal Service Estimated Retainer and Average Case Value

We need an 11x14 flyer that contains the standard retainers and average cost be case, both provided in documents, for each case type we handle. We need the information displayed, preferably in a way that makes the information readable but less troubling to a client shocked at price of litigation. We need one sheet with the retainers and average case value merged into one table.

Target Market(s)

Potential Clients

Font styles to use
Serif
Sans Serif

```html
<!DOCTYPE html>
<html lang="en">
<head>
<meta charset="utf-8">
<title>Legal Service Estimated Retainer and Average Case Value</title>
<link rel="stylesheet" href="https://fonts.googleapis.com/css2?family=EB+Garamond:wght@400;600;700&family=Libre+Baskerville:wght@700&family=Montserrat:wght@400;500&display=swap">
<style>
  :root {
    --page-bg: #e9e6e1;
    --paper: #ffffff;
    --navy: #1b2333;
    --band-dark: #182032;
    --band-teal: #1d4a5c;
    --ink: #1a1a1a;
    --rule: #1c1c1c;
    --cell-light: #ffffff;
    --cell-shade: #cfcfcf;
    --photo-dark: #2a2c31;
    --photo-skin: #c9a28a;
    --photo-light: #e8e2da;
  }
  * { box-sizing: border-box; margin: 0; padding: 0; }
  html, body { width: 1200px; height: 1200px; overflow: hidden; background: var(--page-bg); }
  .flyer {
    position: absolute; left: 143px; top: 20px;
    width: 913px; height: 1160px;
    background: var(--paper);
    box-shadow: 0 6px 20px rgba(0,0,0,.18);
    overflow: hidden;
  }
  .header { position: absolute; left: 0; top: 0; width: 913px; height: 127px; }
  .header-divider { position: absolute; left: 0; top: 0; }
  .firm-name {
    position: absolute; left: 46px; top: 40px;
    display: flex; align-items: center; gap: 14px;
    font-family: "EB Garamond", serif; color: var(--navy);
  }
  .firm-mark { width: 14px; height: 14px; background: var(--navy); }
  .firm-name .small { font-size: 11px; letter-spacing: .5px; display: block; line-height: 1; }
  .firm-name .large { font-size: 25px; letter-spacing: 1px; display: block; line-height: 1; font-weight: 600; }
  .title {
    position: absolute; left: 436px; top: 26px;
    font-family: "Libre Baskerville", serif; font-weight: 700; color: var(--navy);
  }
  .title .main { font-size: 28px; letter-spacing: .3px; line-height: 1.15; }
  .title .sub { font-size: 18.5px; letter-spacing: .2px; margin-top: 4px; }
  .photo {
    position: absolute; left: 0; top: 127px; width: 913px; height: 242px;
    background: linear-gradient(100deg, var(--photo-dark) 0%, #3a3a3e 30%, var(--photo-skin) 50%, #b89580 62%, var(--photo-light) 78%, #1f2126 92%);
  }
  .intro-band {
    position: absolute; left: 0; top: 372px; width: 913px; height: 146px;
    background: radial-gradient(ellipse at 60% 90%, var(--band-teal) 0%, var(--band-dark) 70%);
    padding: 20px 44px 0 45px; color: #fff;
  }
  .intro-band h2 {
    font-family: "EB Garamond", serif; font-weight: 700; font-size: 25px; letter-spacing: .2px; line-height: 1;
  }
  .intro-band p {
    font-family: "Montserrat", sans-serif; font-size: 15.2px; line-height: 20.5px; margin-top: 6px; letter-spacing: .2px;
  }
  .fee-table { position: absolute; left: 0; top: 520px; width: 913px; border-collapse: collapse; table-layout: fixed; }
  .fee-table th {
    background: #000; color: #fff; height: 33px;
    font-family: "EB Garamond", serif; font-weight: 700; font-size: 20px;
  }
  .fee-table td {
    height: 41.3px; text-align: center;
    font-family: "EB Garamond", serif; font-size: 14.5px; color: var(--ink);
    background: linear-gradient(90deg, var(--cell-light) 0%, #f2f2f2 55%, var(--cell-shade) 100%);
    border-bottom: 1.5px solid var(--rule);
  }
  .fee-table td + td { border-left: 2px solid var(--rule); }
  .fee-table td.case { font-size: 13.5px; }
  .fee-table tr:last-child td { border-bottom: 2px solid #888; }
</style>
</head>
<body>
<main class="flyer">
  <header class="header">
    <svg class="header-divider" width="913" height="127" viewBox="0 0 913 127">
      <line x1="423" y1="0" x2="372" y2="127" stroke="#d0d0d0" stroke-width="2"/>
    </svg>
    <div class="firm-name">
      <span class="firm-mark"></span>
      <span><span class="small">THE LAW OFFICE OF</span><span class="large">DANIEL M WHITFORD</span></span>
    </div>
    <div class="title">
      <div class="main">LEGAL SERVICE ESTIMATED</div>
      <div class="sub">RETAINER AND AVERAGE CASE VALUE</div>
    </div>
  </header>

  <div class="photo" role="img" aria-label="Photo of two people in business suits shaking hands"></div>

  <section class="intro-band">
    <h2>THE RETAINER AND THE AVERAGE FEE PER CASE TYPE</h2>
    <p>In order for our clients to set expectations for legal fees, we provide the national average range of &nbsp;fees per case type. These are only to provide you with an understanding of what other cases have cost clients in similar cases. Please note these are not estimates nor guarantees of your own legal costs.</p>
  </section>

  <table class="fee-table">
    <colgroup><col style="width:333px"><col style="width:190px"><col style="width:192px"><col style="width:198px"></colgroup>
    <thead>
      <tr><th></th><th>Average Fee</th><th>Reainter</th><th>Flat Fee</th></tr>
    </thead>
    <tbody>
      <tr><td class="case">Divorce (3301C)</td><td>$2,000 - $1,000</td><td>$2,000</td><td>$2,500</td></tr>
      <tr><td class="case">Divorce (3301D)</td><td>$2,500 - $5,000</td><td>$2,500</td><td>$3,500</td></tr>
      <tr><td class="case">Child/Spousal Support</td><td>-</td><td>-</td><td>$3,000</td></tr>
      <tr><td class="case">Custody Initial Order</td><td>$4,000 - $7,500</td><td>$3,000</td><td>$7,500</td></tr>
      <tr><td class="case">Custody Modification</td><td>$6,500 - $10,000</td><td>$3,500</td><td>-</td></tr>
      <tr><td class="case">Divorce and Custody</td><td>$8,000 - $12,000</td><td>$3,500</td><td>$10,000</td></tr>
      <tr><td class="case">Custody and Support</td><td>$6,000 - $10,000</td><td>$3,000</td><td>$7,500</td></tr>
      <tr><td class="case">Divorce and Support</td><td>$6,500 - $10,000</td><td>$8,000-$12,000</td><td>$8,000</td></tr>
      <tr><td class="case">Divorce and Equitable Distribution</td><td>-</td><td>-</td><td>$10,000</td></tr>
      <tr><td class="case">Divorce, Custody and Support</td><td>$8,000 - $12,000</td><td>$5,000</td><td>$10,000</td></tr>
      <tr><td class="case">Divorce, Equitable Distribution and Support</td><td>$12,500 - $20,000</td><td>$3,500</td><td>$12,500</td></tr>
      <tr><td class="case">Divorce, Equitable Distribution and Custody</td><td>$15,000 - $25,000</td><td>$3,500</td><td>$17,500</td></tr>
      <tr><td class="case">Divorce, Equitable Distribution, Custody and Support</td><td>$5,000 - $30,000</td><td>$3,500</td><td>$20,000</td></tr>
      <tr><td class="case">(PFA) Protection From Abuse</td><td>$2,000</td><td>$2,000</td><td>$2,000</td></tr>
    </tbody>
  </table>
</main>
</body>
</html>
```